Lingerie Shop Flyer Design Project

Looking for a flyer that showcases the shop and the items carried

use the existing website www.parvisonline.com for inspiration about the shop and utilize the existing colors/logo

please contact me with any questions!!!

Is this idea feasible?........maybe a two-sided flyer....one side more "eye catcher"/promotions back side more store info-products.....etc.
Updates

As of 4/9/2013 there is an additional attachment in the brief that hopefully gives a better direction of what the client has in mind.

If you have any additional questions please let me know.

Target Market(s)

affluent women

Industry/Entity Type

Store

Requirements
Must have
• please include address, phone#, location map, hours, email

20% off coupon

$200 gift card drawing

facebook logo

```html
<!DOCTYPE html>
<html lang="en">
<head>
<meta charset="utf-8">
<title>Parvis Lingerie &amp; Loungewear Flyer</title>
<link rel="stylesheet" href="https://fonts.googleapis.com/css2?family=Cormorant+Garamond:wght@500&family=PT+Sans:wght@400;700&family=Josefin+Sans:wght@300&display=swap">
<style>
  :root {
    --crimson: #b31f42;
    --crimson-light: #cc3b5a;
    --crimson-deep: #8e1232;
    --maroon: #5a0c20;
    --band-dark: #2a0610;
    --ink: #3a0a14;
    --white: #ffffff;
    --coupon-grey: #e6e6e6;
    --gift-pink: #e85d86;
    --skin: #e7c2ad;
  }
  * { margin: 0; padding: 0; box-sizing: border-box; }
  html, body { width: 848px; height: 1200px; overflow: hidden; }
  body { font-family: "PT Sans", sans-serif; }
  .flyer {
    position: relative; width: 848px; height: 1200px; overflow: hidden;
    background: radial-gradient(ellipse at 50% 55%, var(--crimson-light) 0%, var(--crimson) 45%, var(--crimson-deep) 100%);
  }
  .brand { position: absolute; left: 50px; top: 34px; width: 190px; text-align: center; color: var(--white); }
  .brand-row { display: flex; align-items: center; justify-content: center; gap: 10px; }
  .brand-dot { width: 14px; height: 14px; border-radius: 50%; background: var(--white); }
  .brand-name { font-family: "Cormorant Garamond", serif; font-weight: 500; font-size: 52px; line-height: 1; }
  .brand-tag { font-family: "Cormorant Garamond", serif; font-weight: 500; font-size: 17px; line-height: 1.15; margin-top: 8px; letter-spacing: 0.5px; }
  .online { position: absolute; right: 46px; top: 56px; text-align: right; }
  .online-lead { color: var(--ink); font-size: 22px; }
  .online-url { color: var(--white); font-size: 24px; margin-top: 4px; }
  .hero-band {
    position: absolute; left: 220px; top: 151px; width: 628px; height: 24px;
    background: var(--crimson-deep); color: var(--white); font-size: 17px; line-height: 24px; padding-left: 20px;
  }
  .hero-photo {
    position: absolute; left: 237px; top: 175px; width: 611px; height: 224px;
    background: linear-gradient(100deg, #ece9ea 0%, #d9cfd0 30%, #2a2226 50%, var(--skin) 75%, #f1ece9 100%);
  }
  .categories {
    position: absolute; left: 0; top: 400px; width: 848px; height: 72px;
    background: linear-gradient(180deg, var(--maroon) 0%, var(--band-dark) 100%);
    display: flex; align-items: center; color: var(--white);
  }
  .categories-title { font-weight: 700; font-size: 24px; margin-left: 64px; letter-spacing: -0.5px; white-space: nowrap; }
  .categories-list { display: flex; gap: 16px; list-style: none; margin-left: 100px; font-size: 13.5px; letter-spacing: -0.4px; white-space: nowrap; }
  .product-card { position: absolute; background: var(--white); padding: 10px; box-shadow: 0 4px 10px rgba(60, 0, 15, 0.45); }
  .product-card .product-photo { width: 100%; height: 100%; }
  .card-pajamas { left: -10px; top: 505px; width: 195px; height: 250px; transform: rotate(-8deg); }
  .card-babydoll { left: 162px; top: 478px; width: 200px; height: 250px; transform: rotate(-9deg); }
  .card-shapewear { left: 275px; top: 492px; width: 230px; height: 225px; transform: rotate(-6deg); }
  .card-robe { left: 470px; top: 500px; width: 205px; height: 255px; transform: rotate(9deg); }
  .card-camisole { left: 675px; top: 470px; width: 200px; height: 290px; transform: rotate(-10deg); }
  .photo-pajamas { background: radial-gradient(circle, #d62a2a 0%, #d62a2a 35%, #fff 70%); }
  .photo-babydoll { background: radial-gradient(ellipse, #1c2550 0%, #1c2550 35%, #fff 70%); }
  .photo-shapewear { background: radial-gradient(ellipse at 50% 30%, #e8cbb2 0%, #e8cbb2 45%, #fff 75%); }
  .photo-robe { background: radial-gradient(ellipse, #6fd6b6 0%, #6fd6b6 35%, #fff 70%); }
  .photo-camisole { background: radial-gradient(ellipse, #f0e8e8 0%, #d9b8a8 50%, #fff 80%); }
  .coupon {
    position: absolute; left: 52px; top: 796px; width: 141px; height: 138px;
    background: linear-gradient(180deg, #fafafa 0%, var(--coupon-grey) 100%);
    border-radius: 6px; box-shadow: 0 3px 8px rgba(60, 0, 15, 0.35);
  }
  .coupon-ribbon {
    position: absolute; left: 8px; top: 0; width: 125px; height: 38px;
    background: linear-gradient(180deg, #d9334f, #a5142f); color: var(--white);
    font-size: 14px; line-height: 16px; text-align: center; padding-top: 3px; letter-spacing: 0.3px;
  }
  .coupon-value { position: absolute; left: 0; top: 48px; width: 100%; text-align: center; color: #e01e35; font-weight: 700; font-size: 58px; line-height: 1.2; }
  .gift-card {
    position: absolute; left: 51px; top: 980px; width: 272px; height: 163px;
    background: var(--white); border: 3px dotted var(--gift-pink); padding: 12px 12px;
  }
  .gift-title { font-family: "Josefin Sans", sans-serif; font-weight: 300; color: var(--gift-pink); font-size: 38px; letter-spacing: 2px; line-height: 1; }
  .gift-body { display: flex; align-items: center; gap: 10px; margin-top: 18px; }
  .gift-amount {
    flex: none; width: 60px; height: 60px; border-radius: 50%; background: var(--gift-pink);
    color: #fbc6d6; font-family: "Josefin Sans", sans-serif; font-weight: 300; font-size: 21px; line-height: 60px; text-align: center;
  }
  .gift-text { color: var(--gift-pink); font-size: 10px; line-height: 2; white-space: nowrap; }
  .info { position: absolute; color: var(--white); font-size: 11.5px; line-height: 1.7; }
  .info h3 { font-size: 11.5px; font-weight: 700; margin-bottom: 3px; }
  .info-address { left: 417px; top: 793px; }
  .info-phone { left: 601px; top: 793px; }
  .info-web { left: 417px; top: 897px; }
  .info-hours { left: 601px; top: 897px; }
  .location-map {
    position: absolute; left: 600px; top: 970px; width: 232px; height: 165px;
    background: linear-gradient(135deg, rgba(255,255,255,0.22) 0%, rgba(255,255,255,0.1) 100%);
    border-radius: 4px;
  }
</style>
</head>
<body>
<main class="flyer">
  <header class="brand">
    <div class="brand-row"><span class="brand-dot"></span><span class="brand-name">Parvis</span></div>
    <p class="brand-tag">LINGERIE &amp;<br>LOUNGEWEAR</p>
  </header>

  <div class="online">
    <p class="online-lead">Visit our online store!</p>
    <p class="online-url">www.parvisonline.com</p>
  </div>

  <div class="hero-band">LINGERIE &amp; LOUNGEWEAR</div>
  <div class="hero-photo" role="img" aria-label="Photo of a smiling woman lying on white sheets wearing black lace lingerie"></div>

  <nav class="categories">
    <span class="categories-title">Categories</span>
    <ul class="categories-list">
      <li>Pajamas/Loungewear</li>
      <li>Chemises/Babydolls/Teddies</li>
      <li>Shapewear</li>
      <li>Fragrances</li>
      <li>Robes</li>
      <li>Bridal</li>
    </ul>
  </nav>

  <figure class="product-card card-pajamas"><div class="product-photo photo-pajamas" role="img" aria-label="Red cami and shorts pajama set with black trim"></div></figure>
  <figure class="product-card card-babydoll"><div class="product-photo photo-babydoll" role="img" aria-label="Navy sheer babydoll chemise"></div></figure>
  <figure class="product-card card-shapewear"><div class="product-photo photo-shapewear" role="img" aria-label="Nude shaping tank top"></div></figure>
  <figure class="product-card card-robe"><div class="product-photo photo-robe" role="img" aria-label="Mint green floral robe"></div></figure>
  <figure class="product-card card-camisole"><div class="product-photo photo-camisole" role="img" aria-label="White lace camisole"></div></figure>

  <section class="coupon">
    <div class="coupon-ribbon">DISCOUNT<br>COUPON</div>
    <div class="coupon-value">20%</div>
  </section>

  <section class="gift-card">
    <h2 class="gift-title">GIFT CARD</h2>
    <div class="gift-body">
      <div class="gift-amount">$200</div>
      <p class="gift-text">Hey, I am a TWO Hundred DOLLAR<br>giftcard from PARVIS.SHOPCART.COM<br>Feel free to use me now!</p>
    </div>
  </section>

  <section class="info info-address">
    <h3>ADDRESS</h3>
    <p>2750 Linden Court, Suite 210<br>Fairhaven, MO 63190<br>USA</p>
  </section>
  <section class="info info-phone">
    <h3>TELEPHONE &amp; FAX</h3>
    <p>555.214.3380 &amp; 555.214.3391</p>
  </section>
  <section class="info info-web">
    <h3>WEB &amp; E-mail</h3>
    <p>info@parvisonline.com<br>www.parvisonline.com</p>
  </section>
  <section class="info info-hours">
    <h3>Hours of Operation</h3>
    <p>Monday to Friday: 10:00 a.m. to 6:00 p.m.<br>Saturday: 10:00 a.m. to 5:00 p.m.<br>Sunday: Closed</p>
  </section>

  <div class="location-map" role="img" aria-label="Location map showing the roads and highway interchange near the store"></div>
</main>
</body>
</html>
```